IT Company based on Biology Business Needs a PowerPoint Design

We need a powerpoint design for a new company called 'Vast KELP'. We develop the machine learning solutions especially focused on deep learning algorithms for biology industry. Our initial product is a vision detection on biological images to help doctors diagnose the symptoms. We would like to see designs that use the color green.

Industry/Entity Type

Biotechnology

Requirements
Nice to have
• Lots of slide templates with company logo's look and feel

```html
<!DOCTYPE html>
<html lang="en">
<head>
<meta charset="utf-8">
<title>Vast KELP – Slide Templates</title>
<link rel="stylesheet" href="https://fonts.googleapis.com/css2?family=Open+Sans:wght@400&family=Questrial&family=PT+Sans:wght@400&display=swap">
<style>
  :root{
    --green-bright:#25d000;
    --green-mid:#1fb800;
    --green-deep:#1a5a12;
    --green-lime:#8ee82a;
    --green-text:#2c6e12;
    --white:#ffffff;
    --ink:#111111;
    --dots:rgba(255,255,255,.75);
    --dots-dark:rgba(60,60,60,.7);
  }
  *{box-sizing:border-box;margin:0;padding:0}
  html,body{width:1194px;height:1200px;overflow:hidden;background:var(--white)}
  .canvas{position:relative;width:1194px;height:1200px}

  .slide{position:absolute;overflow:hidden}
  .slide--title{left:45px;top:49px;width:716px;height:543px;
    background:radial-gradient(ellipse 85% 95% at 30% 30%,var(--green-bright) 0%,var(--green-mid) 45%,var(--green-deep) 100%)}
  .slide--content{left:45px;top:623px;width:714px;height:541px;
    background:radial-gradient(ellipse 90% 90% at 20% 20%,var(--green-bright) 0%,var(--green-mid) 50%,var(--green-deep) 100%)}

  .helix{position:absolute}
  .helix--left{left:0;top:0;width:187px;height:543px;
    background:linear-gradient(180deg,rgba(170,250,60,.35),rgba(120,230,40,.2) 50%,rgba(170,250,60,.4))}
  .helix--top-right{right:0;top:0;width:97px;height:145px;
    background:linear-gradient(180deg,rgba(140,240,40,.6),rgba(40,200,0,.5))}
  .helix--bottom-left{left:0;bottom:0;width:102px;height:149px;
    background:linear-gradient(180deg,rgba(140,240,40,.6),rgba(40,200,0,.5))}

  .placeholder{position:absolute;border:1px dotted var(--dots)}
  .slide--title .placeholder--title{left:145px;top:18px;width:545px;height:186px}
  .slide--title .placeholder--subtitle{left:145px;top:206px;width:545px;height:134px}
  .title-text{position:absolute;right:10px;bottom:4px;
    font-family:"Open Sans",sans-serif;font-size:39px;color:var(--white);line-height:1}
  .subtitle-text{position:absolute;right:10px;top:2px;
    font-family:"Open Sans",sans-serif;font-size:21px;color:var(--green-lime);line-height:1}

  .brand{position:absolute;display:flex;align-items:center;gap:8px}
  .brand__dot{border-radius:50%;background:var(--green-lime)}
  .brand__name{font-family:"Open Sans",sans-serif;color:var(--green-lime);line-height:1;white-space:nowrap}
  .slide--title .brand{left:505px;top:440px}
  .slide--title .brand__dot{width:20px;height:20px}
  .slide--title .brand__name{font-size:34px}

  .panel{position:absolute;left:22px;top:23px;width:672px;height:499px;background:var(--white);
    box-shadow:3px 4px 6px rgba(0,0,0,.5)}
  .panel .placeholder{border-color:var(--dots-dark)}
  .panel .placeholder--title{left:23px;top:5px;width:624px;height:106px}
  .panel .placeholder--body{left:23px;top:119px;width:624px;height:349px}
  .content-title{position:absolute;left:8px;top:32px;font-family:"Questrial",sans-serif;
    font-size:40px;color:var(--green-text);line-height:1}
  .content-bullet{position:absolute;left:8px;top:8px;font-family:"Questrial",sans-serif;
    font-size:26px;color:var(--green-text);line-height:1}
  .content-bullet::before{content:"•";font-size:14px;margin-right:10px;vertical-align:middle}
  .insert-icons{position:absolute;left:246px;top:134px}
  .panel .brand{left:530px;top:440px}
  .panel .brand__dot{width:16px;height:16px}
  .panel .brand__name{font-size:23px}

  .label{position:absolute;left:845px;font-family:"PT Sans",sans-serif;font-size:36px;color:var(--ink);line-height:1}
  .label--title{top:296px}
  .label--slide{top:902px}
</style>
</head>
<body>
<main class="canvas">

  <section class="slide slide--title">
    <div class="helix helix--left" role="img" aria-label="Decorative DNA strand pattern in light greens"></div>
    <div class="placeholder placeholder--title"><span class="title-text">Click to add title</span></div>
    <div class="placeholder placeholder--subtitle"><span class="subtitle-text">Click to add subtitle</span></div>
    <div class="brand"><span class="brand__dot"></span><span class="brand__name">VAST KELP</span></div>
  </section>

  <section class="slide slide--content">
    <div class="helix helix--top-right" role="img" aria-label="Decorative DNA strand pattern in greens"></div>
    <div class="helix helix--bottom-left" role="img" aria-label="Decorative DNA strand pattern in greens"></div>
    <div class="panel">
      <div class="placeholder placeholder--title"><span class="content-title">Click to add title</span></div>
      <div class="placeholder placeholder--body">
        <span class="content-bullet">Click to add text</span>
        <svg class="insert-icons" width="134" height="86" viewBox="0 0 134 86" aria-label="Insert content icons">
          <g fill="none" stroke="#9fb4c4" stroke-width="1">
            <rect x="1" y="1" width="36" height="32" fill="#eef3f7"/>
            <line x1="1" y1="9" x2="37" y2="9"/><line x1="1" y1="17" x2="37" y2="17"/><line x1="1" y1="25" x2="37" y2="25"/>
            <line x1="13" y1="1" x2="13" y2="33"/><line x1="25" y1="1" x2="25" y2="33"/>
          </g>
          <rect x="49" y="14" width="8" height="19" fill="#8ec5ea"/>
          <rect x="59" y="1" width="8" height="32" fill="#f5d9a6"/>
          <rect x="69" y="9" width="8" height="24" fill="#b9c3c9"/>
          <path d="M94 1h20l6 6v26H94z" fill="#eef3f7" stroke="#9fb4c4"/>
          <path d="M94 4h16l-4 8h-12z" fill="#bfe8cf"/>
          <g fill="none" stroke="#9fb4c4">
            <rect x="1" y="50" width="36" height="33" fill="#eef3f7"/>
            <rect x="49" y="50" width="36" height="33" fill="#eef3f7"/>
            <rect x="96" y="50" width="36" height="33" fill="#eef3f7"/>
            <circle cx="29" cy="72" r="8" stroke="#6fb3e0" fill="#ffffff"/>
            <circle cx="77" cy="72" r="8" stroke="#6fb3e0" fill="#ffffff"/>
            <circle cx="124" cy="72" r="8" stroke="#6fb3e0" fill="#ffffff"/>
          </g>
          <circle cx="28" cy="57" r="3" fill="#f5c98a"/>
          <circle cx="76" cy="57" r="3" fill="#f5c98a"/>
        </svg>
      </div>
      <div class="brand"><span class="brand__dot"></span><span class="brand__name">VAST KELP</span></div>
    </div>
  </section>

  <p class="label label--title">Title Background</p>
  <p class="label label--slide">Slide Background</p>

</main>
</body>
</html>
```